Martial Arts Website

Redevelopment of existing martial arts website.

The academy teaches traditional shaolin martial arts, including Shaolin Kung Fu, Wu Shu, Tai Chi, Qigong and Wing Chun and the site needs to reflect the traditional roots (eg, no tacky boxing imagery)

Existing website is www.copperheron.com.au to get a feel for the desired color scheme (black, green and red). The exact colors can be tweaked though. Please only reuse the logo and font (Karate) - there isnt anything else from the current design that needs to remain.

The current website includes links to a YouTube channel that includes demonstrations of the training conducted to better guide the design.

The new website site map will be:
1. Home
2. Programs - summary page describing each form of training
a. Tiny Sparrows
b. Kids Kung Fu
c. Youth Kung Fu
d. Adults Kung Fu
e. Wing Chun
f. Tai Chi & Qigong
g. Weaponry Classes
h. 48 Paths of Mountain Endurance Program
i. Acrobatics and Wu Shu
j. Fitness Boxing
3. Timetable
4. Coaches - summary page describing all coaches
a. Sifu (Master)
b. Sihing Lars
c. Sihing Kit
d. Sihing Gordon
X. ... up to 10 or so coaches
5. Member Zone
6. Contact Us
Updates

Logo now attached to brief - sorry I only have it in PDF

Just to clarify, I am only expecting a PSD design - no HTML required

Project Deadline Extended
Reason: Thanks for the designs, we love a lot of them just require a little extra time to tweak the designs and establish the potential. Thanks for your understanding and efforts.

Target Market(s)

Parents, teenagers, young adults, adults, elderly

Industry/Entity Type

Training

Requirements
Must have
• Chinese kung fu dragon imagery throughout the background
Links to Friendbook and YouTube channel
Promo/icon in the header "Try 2 free classes now"
Home page should include an embedded YouTube video

```html
<!DOCTYPE html>
<html lang="en">
<head>
<meta charset="utf-8">
<title>Jade Serpent Martial Arts Academy</title>
<link href="https://fonts.googleapis.com/css2?family=Ribeye&family=Ubuntu:ital,wght@0,400;1,400&family=Open+Sans:wght@400&display=swap" rel="stylesheet">
<style>
:root{
  --page:#262626;
  --green-dark:#1d5a12;
  --lime:#98c21c;
  --sage:#8fae4f;
  --red:#8a1a22;
  --red-dark:#5a0c13;
  --cream:#f2fbd9;
  --text-light:#ffffff;
  --footer-text:#f1d6d6;
}
*{margin:0;padding:0;box-sizing:border-box}
html,body{width:1200px;height:1200px;overflow:hidden;background:var(--page)}
body{position:relative;font-family:"Ubuntu",sans-serif;color:var(--text-light)}
.abs{position:absolute}
.title-band{left:0;top:20px;width:1200px;height:70px;background:linear-gradient(#58b73a,#2f8a1f 60%,#22701a);border-top:2px solid #7fd25c;border-bottom:2px solid #174d10}
.site-title{left:300px;top:34px;width:866px;font-family:"Ribeye",serif;font-size:31px;font-weight:400;letter-spacing:2px;color:#e9f7df;text-shadow:2px 2px 0 #0f2e0a,-1px -1px 0 #0f2e0a;white-space:nowrap;text-align:justify;text-align-last:justify}
.header{left:0;top:92px;width:1200px;height:240px;background:repeating-linear-gradient(45deg,#2f2d29 0 3px,#29271f 3px 6px)}
.banner{left:52px;top:10px;width:221px;height:306px}
.logo-box{left:92px;top:38px;width:141px;height:139px;background:#fff;border:2px solid #ccc;display:flex;flex-direction:column;align-items:center;justify-content:center;gap:8px}
.logo-box .dot{width:22px;height:22px;border-radius:50%;background:#2f8a1f}
.logo-box span{font-size:15px;color:#1d5a12;text-align:center;line-height:1.2}
.quote{left:340px;top:137px;font-size:19px;line-height:23px;text-shadow:1px 1px 2px #000}
.quote p{white-space:nowrap}
.hero-photo{left:758px;top:93px;width:382px;height:238px;background:linear-gradient(#3a3e52,#a06a4a 45%,#f0a24a 70%,#1b1712 88%)}
.nav{left:0;top:332px;width:1200px;height:45px;background:linear-gradient(#4fb235,#2a8720 50%,#1c6a14);border-top:1px solid #7fd25c;border-bottom:1px solid #144a0e}
.nav ul{list-style:none;position:absolute;left:340px;top:0;display:flex;height:45px}
.nav li{font-style:italic;font-size:20px;padding:10px 20px 0;position:relative;text-shadow:1px 1px 2px #0b2a07}
.nav li+li::before{content:"";position:absolute;left:0;top:2px;height:42px;border-left:1px solid #8fd36e;transform:skewX(-25deg)}
.sidebar{left:49px;top:377px;width:314px;height:763px;background:var(--sage)}
.classes{left:68px;top:395px;width:286px;height:656px;border:6px solid var(--green-dark);border-radius:14px;background:var(--lime);overflow:hidden}
.dragon-texture{left:74px;top:640px;width:274px;height:330px;background:radial-gradient(ellipse at 60% 50%,rgba(60,100,10,.35),rgba(60,100,10,0) 70%)}
.classes-head{height:56px;background:linear-gradient(#2c6a18,#4f8e22);border-bottom:2px solid #c23a2a;text-align:center;font-family:"Ribeye",serif;font-size:34px;color:#2e7a10;text-shadow:1px 1px 0 #0e2a06;padding-top:6px;letter-spacing:2px}
.class-list{list-style:none;padding-top:26px;position:relative}
.class-list li{height:60px;border-bottom:1px solid #6f941a;padding:3px 0 0 24px}
.class-list li:last-child{border-bottom:none}
.class-name{font-size:21px;text-shadow:1px 1px 2px #3a5a08}
.class-desc{font-style:italic;font-size:16px;color:#111;padding-left:14px}
.social{top:1065px;width:58px;height:58px;border-radius:8px;background:#e9eef2;border:1px solid #9aa;display:flex;align-items:center;justify-content:center;font-size:10px;color:#2d4f7a}
.main{left:363px;top:377px;width:787px;height:429px;background:linear-gradient(90deg,#0a0a0a,#1c2a10 50%,#2b3a12)}
.welcome{left:422px;top:412px;font-family:"Ribeye",serif;font-size:34px;font-weight:400;color:#7fbf2a;text-shadow:0 0 8px #9f6,1px 1px 0 #103;letter-spacing:1px}
.intro{left:413px;top:482px;width:405px;font-family:"Open Sans",sans-serif;font-size:15px;line-height:18.2px;letter-spacing:.45px;color:#f2f2f2;hyphens:auto}
.intro-photo{left:406px;top:665px;width:172px;height:127px;background:radial-gradient(#5c6a86,#1a1a1f 75%)}
.newsletter{left:605px;top:733px;width:314px;height:48px;border-radius:10px;background:linear-gradient(90deg,#1e3a10,#3d6e1c);border:2px solid #5c8a2a;font-family:"Open Sans",sans-serif;font-size:15px;padding:12px 0 0 102px;letter-spacing:.5px}
.news-icon{left:620px;top:708px;width:70px;height:66px;background:linear-gradient(#f2f2ee,#c9c9c2);border-radius:4px;transform:rotate(-18deg)}
.accred{left:1008px;top:385px;width:153px;height:400px;background:linear-gradient(var(--red),var(--red-dark) 85%,#111)}
.accred-inner{left:1021px;top:398px;width:130px;height:372px;background:linear-gradient(#7d8c63,#5e6d47 85%,#222)}
.accred-label{width:100px;text-align:center;font-size:15px;color:#1a1a1a;border-bottom:1px solid #222;padding-bottom:2px}
.badge{background:#f4f4f4;border:1px solid #222;box-shadow:2px 2px 3px #222}
.news{left:363px;top:806px;width:787px;height:324px;background:linear-gradient(#dbe8b6,#b6c98a 40%,#6f7f55 80%,#2f3525)}
.news-title{left:508px;top:815px;font-family:"Ribeye",serif;font-size:34px;font-weight:400;color:#256b0d;text-shadow:1px 1px 0 #0c2a05}
.news-box{left:392px;top:866px;width:337px;height:215px;background:var(--cream);border:1px solid #555;box-shadow:2px 2px 5px #333;padding:16px 6px 0 13px;font-family:"Open Sans",sans-serif;font-size:14px;line-height:16.5px;color:#111}
.news-box p{margin-bottom:10px}
.news-box em{font-style:normal;color:#c0000a}
.video-frame{left:760px;top:842px;width:402px;height:250px;background:linear-gradient(90deg,#6d7f4f,#8fa06a,#6d7f4f);border:1px solid #3a4a25;box-shadow:3px 3px 6px #222}
.video{left:789px;top:867px;width:342px;height:210px;background:#000}
.video-scene{left:831px;top:867px;width:258px;height:190px;background:linear-gradient(#c9c9cf,#8d8f99 55%,#5fb7b0)}
.video-bar{left:789px;top:1057px;width:342px;height:20px;background:#1b1b1b;border-top:3px solid #c00}
.bottom-band{left:363px;top:1130px;width:787px;height:10px;background:#111}
.footer-copy{left:75px;top:1159px;font-family:"Open Sans",sans-serif;font-size:15px;color:var(--footer-text)}
.footer-nav{left:620px;top:1157px;font-family:"Open Sans",sans-serif;font-size:15px;color:var(--footer-text);white-space:nowrap}
</style>
</head>
<body>
<div class="abs header"></div>
<div class="abs title-band"></div>
<h1 class="abs site-title">JADE SERPENT MARTIAL ARTS ACADEMY</h1>

<svg class="abs banner" viewBox="0 0 221 306" aria-hidden="true">
  <defs><radialGradient id="bn" cx="50%" cy="40%" r="70%"><stop offset="0" stop-color="#9a1d2a"/><stop offset="1" stop-color="#5c0a14"/></radialGradient></defs>
  <path d="M1 1H220V305L110 238 1 305Z" fill="url(#bn)" stroke="#2a0a0c" stroke-width="2"/>
  <path d="M14 14H207V280L110 222 14 280Z" fill="none" stroke="#8a6a6c" stroke-width="3" opacity=".7"/>
</svg>
<div class="abs logo-box"><div class="dot"></div><span>Jade Serpent</span></div>

<blockquote class="abs quote">
  <p>“Martial Arts Quote</p>
  <p style="padding-left:38px">Martial Arts Quote</p>
  <p style="padding-left:74px">Mind, Body and Soul</p>
  <p style="padding-left:38px">Dragon Fury and Kung Fu”</p>
  <p style="padding-left:182px">-Wen Lai</p>
</blockquote>
<div class="abs hero-photo" role="img" aria-label="Tai chi practitioner in a low stance at sunset"></div>

<nav class="abs nav"><ul>
  <li>Home</li><li>Programs</li><li>Timetable</li><li>Coaches</li><li>Member Zone</li><li>Contact Us</li>
</ul></nav>

<aside class="abs sidebar"></aside>
<section class="abs classes">
  <div class="classes-head">CLASSES</div>
  <ul class="class-list">
    <li><div class="class-name">Tiny Sparrows</div><div class="class-desc">Small Description</div></li>
    <li><div class="class-name">Kids Kung Fu</div><div class="class-desc">Small Description</div></li>
    <li><div class="class-name">Youth Kung Fu</div><div class="class-desc">Small Description</div></li>
    <li><div class="class-name">Adults Kung Fu</div><div class="class-desc">Small Description</div></li>
    <li><div class="class-name">Wing Chun</div><div class="class-desc">Small Description</div></li>
    <li><div class="class-name">Tai Chi &amp; Qigong</div><div class="class-desc">Small Description</div></li>
    <li><div class="class-name">Weaponry Classes</div><div class="class-desc">Small Description</div></li>
    <li><div class="class-name">48 Paths of Mountain</div><div class="class-desc">Small Description</div></li>
    <li><div class="class-name">Performance Team</div><div class="class-desc">Small Description</div></li>
  </ul>
</section>
<div class="abs dragon-texture" role="img" aria-label="Faint Chinese dragon motif behind the class list"></div>
<div class="abs social" style="left:105px">Friendbook</div>
<div class="abs social" style="left:180px">Searchly</div>
<div class="abs social" style="left:254px">Chirper</div>

<main class="abs main"></main>
<svg class="abs" style="left:363px;top:377px" width="787" height="429" viewBox="0 0 787 429" aria-hidden="true">
  <path d="M560 0H787V429H400Q600 400 605 230Q610 80 560 0Z" fill="#8b2a2e"/>
</svg>
<h2 class="abs welcome">WELCOME...</h2>
<p class="abs intro">&emsp;&ensp;Lorem ipsum dolor sit amet, consectetur adip&shy;isicing elit, sed do eiusmod tempor incididunt ut labore et dolore magna aliqua. Ut enim ad minim veniam, quis nostrud exercitation ullamco laboris nisi ut aliquip ex ea commodo consequat. Duis aute irure dolor in reprehenderit in voluptate velit esse cillum dolore eu fugiat nulla pariatur. Excepteur sint occaecat cupidatat non proident, sunt in culpa qui officia deserunt mollit anim id est laborum.</p>
<div class="abs intro-photo" role="img" aria-label="Kung fu student posing before a pagoda"></div>
<div class="abs newsletter">Download our Newsletter!</div>
<div class="abs news-icon" role="img" aria-label="Folded newspaper"></div>

<div class="abs accred"></div>
<div class="abs accred-inner"></div>
<div class="abs accred-label" style="left:1036px;top:403px">Accreditation</div>
<div class="abs badge" style="left:1054px;top:433px;width:66px;height:66px;border-radius:50%"></div>
<div class="abs badge" style="left:1054px;top:509px;width:72px;height:50px;border-radius:6px"></div>
<div class="abs badge" style="left:1059px;top:571px;width:62px;height:50px"></div>
<div class="abs accred-label" style="left:1036px;top:639px">Alliances</div>
<div class="abs badge" style="left:1055px;top:673px;width:66px;height:74px;background:#8a8a7a"></div>

<section class="abs news"></section>
<h2 class="abs news-title">NEWS</h2>
<svg class="abs" style="left:398px;top:818px" width="330" height="30" aria-hidden="true">
  <path d="M12 22H80M250 22H318" stroke="#2f5a18" stroke-width="3"/>
  <circle cx="12" cy="22" r="6" fill="none" stroke="#2f5a18" stroke-width="2"/>
  <circle cx="318" cy="22" r="6" fill="none" stroke="#2f5a18" stroke-width="2"/>
</svg>
<div class="abs" style="left:744px;top:840px;width:1px;height:260px;background:#4f6a2a"></div>
<div class="abs news-box">
  <p>-Lorem ipsum dolor sit amet, consectetur adipisicing elit, sed do eiusmod tempor incididunt ut labore et dolore <em>magna aliqua.</em></p>
  <p>-Lorem ipsum dolor sit amet, consectetur adipisicing elit, sed do eiusmod tempor incididunt ut labore et dolore <em>magna aliqua.</em></p>
  <p>-Lorem ipsum dolor sit amet, consectetur adipisicing elit, sed do eiusmod tempor incididunt ut labore et dolore <em>magna aliqua.</em></p>
</div>
<div class="abs video-frame"></div>
<div class="abs video"></div>
<div class="abs video-scene" role="img" aria-label="Embedded training demonstration video"></div>
<div class="abs video-bar"></div>
<div class="abs bottom-band"></div>

<footer>
  <p class="abs footer-copy">Copyright ©2012 Jade Serpent Martial Arts Academy</p>
  <p class="abs footer-nav">Home | Programs | Timetable | Coaches | Member Zone | Contact Us</p>
</footer>
</body>
</html>
```